Open Door Dialogues: Classroom and Family Allies building brighter pupil futures.

This is a book that helps to prepare for and hold a standard conference that an educator would have with the parents of the students in the school. It is also about how to have problem-solving conferences around difficult issues using techniques from family therapy. Parent involvement is a key ingredient for student success, but most educators have no training in holding meetings with parents. This book fills that gap.

Target Market(s)

Teachers, principals, counselors, school psychologists, school nurses. Anyone who has conferences with the parents of their students.

Font styles to use
Sans Serif

Colors
85acd3
ffcf3e

Requirements
Must have
• I have several books coming up. I'd like something that could be carried over to the new ones without too many changes. They won't all be about education. I am a psychologist so most of my writings will cover subjects related to emotional intelligence.
Nice to have
• Something dignified that will pop out for those in the schools. I like the combination of a royal blue background with white and gold (not yellow) lettering.
Should not have
• I'd like it to be easy to read. Not too messy or too much stuff on the page.

```html
<!DOCTYPE html>
<html lang="en">
<head>
<meta charset="UTF-8">
<title>Open Door Dialogues — Book Cover</title>
<link rel="stylesheet" href="https://fonts.googleapis.com/css2?family=Jost:wght@500;700&family=Crimson+Text&display=swap">
<style>
  :root {
    --navy: #001244;
    --gold: #b5873a;
    --cream: #fbf6ea;
    --white: #ffffff;
  }
  html, body {
    margin: 0;
    padding: 0;
    overflow: hidden;
    background: var(--navy);
  }
  .cover {
    position: relative;
    width: 933px;
    height: 1200px;
    background: var(--navy);
    overflow: hidden;
  }
  .title {
    position: absolute;
    left: 0;
    top: 0;
    width: 100%;
    margin: 0;
    font-family: "Jost", sans-serif;
    font-weight: 700;
    text-transform: uppercase;
    text-align: center;
  }
  .title-line {
    position: absolute;
    left: 0;
    width: 100%;
    display: block;
    line-height: 1;
    letter-spacing: 0.01em;
  }
  .title-line span {
    display: inline-block;
    background: linear-gradient(to bottom, var(--gold) 0%, var(--gold) 38%, var(--cream) 82%, var(--cream) 100%);
    -webkit-background-clip: text;
    background-clip: text;
    color: transparent;
  }
  .title-line--major {
    font-size: 176px;
  }
  .title-line--first { top: 68px; }
  .title-line--second { top: 221px; }
  .title-line--minor {
    top: 407px;
    font-size: 94px;
  }
  .subtitle {
    position: absolute;
    left: 0;
    top: 560px;
    width: 100%;
    margin: 0;
    font-family: "Crimson Text", serif;
    font-size: 39px;
    line-height: 58px;
    color: var(--white);
    text-align: center;
  }
  .author {
    position: absolute;
    right: 96px;
    top: 1121px;
    margin: 0;
    font-family: "Jost", sans-serif;
    font-weight: 500;
    font-size: 37px;
    line-height: 1;
    color: var(--gold);
    text-transform: uppercase;
  }
</style>
</head>
<body>
  <main class="cover">
    <h1 class="title">
      <span class="title-line title-line--major title-line--first"><span>Open</span></span>
      <span class="title-line title-line--major title-line--second"><span>Door</span></span>
      <span class="title-line title-line--minor"><span>Dialogues</span></span>
    </h1>
    <p class="subtitle">Classroom and Family Allies building<br>brighter pupil futures.</p>
    <p class="author">Author Name</p>
  </main>
</body>
</html>
```